indépendant en tant que Massothérapeute et Préparateur Mental, j'ai besoin de ...

Massothérapeute et préparateur mental indépendant, je recherche une carte de visite sobre et dynamique, sans images liées au massage ou à la préparation mentale mais intégrant mon logo. Les couleurs que j'aime bien sont : Blanc, gris, anthracite, noir et jaune

Contact Information for Business Card

carte de préférence Horizontale
neutre qui puisse toucher le deux domaines Massothérapie et préparation mentale

Requirements
Must have
• mon projet doit intégrer au recto:
LOGO
Loïc Vermande
078 315 26 49
info@loicvermande-exemple.ch
et éventuellement www.loicvermande-exemple.ch

et au verso les deux adresses:

Chemin des Ormelets 27B
1400 Yverdon-les-Bains

Rue des Tanneries 9
1700 Fribourg

Should not have
• mon projet ne doit pas contenir d'image en liens avec le massage ni la préparation mentale.

```html
<!DOCTYPE html>
<html lang="fr">
<head>
<meta charset="utf-8">
<title>Loïc Vermande – Carte de visite</title>
<link href="https://fonts.googleapis.com/css2?family=Open+Sans:wght@400;600&display=swap" rel="stylesheet">
<style>
  :root {
    --backdrop: #e6e6e6;
    --anthracite: #2d2c2a;
    --card-light: #f3f3f3;
    --ink: #2f2f2f;
    --ink-soft: #3a3a3a;
    --mark-on-dark: #6a6a6a;
    --rule: #333333;
  }
  html, body {
    margin: 0;
    padding: 0;
    width: 1200px;
    height: 960px;
    overflow: hidden;
    background: var(--backdrop);
    font-family: "Open Sans", Arial, sans-serif;
  }
  .canvas {
    position: relative;
    width: 1200px;
    height: 960px;
  }
  .card {
    position: absolute;
    left: 323px;
    width: 557px;
    height: 361px;
    box-sizing: border-box;
  }
  .card--front { top: 102px; background: var(--anthracite); }
  .card--back  { top: 495px; background: var(--card-light); }

  .brand {
    position: absolute;
    left: 0;
    right: 0;
    display: flex;
    justify-content: center;
    align-items: center;
    gap: 16px;
  }
  .card--front .brand { top: 160px; }
  .card--back .brand  { top: 58px; }
  .brand__square {
    width: 34px;
    height: 34px;
    flex: none;
  }
  .brand__text { display: flex; flex-direction: column; }
  .brand__name {
    font-size: 30px;
    font-weight: 600;
    line-height: 1.05;
    letter-spacing: 0.5px;
  }
  .brand__role {
    font-size: 11px;
    font-weight: 600;
    letter-spacing: 0.6px;
    margin-top: 3px;
  }
  .card--front .brand__square { background: var(--mark-on-dark); }
  .card--front .brand__name,
  .card--front .brand__role { color: var(--mark-on-dark); }
  .card--back .brand__square { background: var(--ink); }
  .card--back .brand__name,
  .card--back .brand__role { color: var(--ink); }

  .holder {
    position: absolute;
    top: 211px;
    right: 300px;
    margin: 0;
    font-size: 19px;
    font-weight: 600;
    color: var(--ink-soft);
    letter-spacing: 0.3px;
  }
  .divider {
    position: absolute;
    left: 278px;
    top: 192px;
    width: 1px;
    height: 64px;
    background: var(--rule);
  }
  .contact {
    position: absolute;
    left: 298px;
    top: 194px;
    margin: 0;
    padding: 0;
    list-style: none;
    font-size: 14px;
    color: var(--ink);
  }
  .contact li {
    display: flex;
    align-items: center;
    gap: 8px;
    height: 20px;
  }
  .contact svg { width: 13px; height: 13px; flex: none; }
  .addresses {
    position: absolute;
    left: 0;
    right: 0;
    top: 284px;
    margin: 0;
    text-align: center;
    font-size: 14px;
    line-height: 20px;
    color: var(--ink);
    font-style: normal;
  }
</style>
</head>
<body>
<main class="canvas">
  <section class="card card--front" aria-label="Recto">
    <div class="brand">
      <span class="brand__square"></span>
      <div class="brand__text">
        <span class="brand__name">Loïc Vermande</span>
        <span class="brand__role">MASSOTHÉRAPEUTE / PRÉPARATEUR MENTAL</span>
      </div>
    </div>
  </section>

  <section class="card card--back" aria-label="Verso">
    <div class="brand">
      <span class="brand__square"></span>
      <div class="brand__text">
        <span class="brand__name">Loïc Vermande</span>
        <span class="brand__role">MASSOTHÉRAPEUTE / PRÉPARATEUR MENTAL</span>
      </div>
    </div>

    <h1 class="holder">LOÏC VERMANDE</h1>
    <span class="divider"></span>
    <ul class="contact">
      <li>
        <svg viewBox="0 0 16 16" aria-hidden="true"><path fill="#2f2f2f" d="M3.6 1.2l2.3 2.6-1.3 1.7c.9 2 2.6 3.7 4.6 4.6l1.7-1.3 2.6 2.3-1.3 2.3c-5.4-.5-9.7-4.8-10.2-10.2z"/></svg>
        <span>078 315 26 49</span>
      </li>
      <li>
        <svg viewBox="0 0 16 16" aria-hidden="true"><rect x="1" y="3" width="14" height="10" fill="none" stroke="#2f2f2f" stroke-width="1.6"/><path d="M1.5 3.5L8 9l6.5-5.5" fill="none" stroke="#2f2f2f" stroke-width="1.6"/></svg>
        <span>info@loicvermande-exemple.ch</span>
      </li>
      <li>
        <svg viewBox="0 0 16 16" aria-hidden="true"><g fill="none" stroke="#2f2f2f" stroke-width="1.3"><circle cx="8" cy="8" r="6.5"/><ellipse cx="8" cy="8" rx="2.8" ry="6.5"/><path d="M1.5 8h13M2.5 4.8h11M2.5 11.2h11"/></g></svg>
        <span>www.loicvermande-exemple.ch</span>
      </li>
    </ul>

    <address class="addresses">
      Chemin des Ormelets 27B, 1400 Yverdon-les-Bains<br>
      Rue des Tanneries 9, 1700 Fribourg
    </address>
  </section>
</main>
</body>
</html>
```